Global Nano Technology Surface Protection company needs a new logo and cards

We are a Global company that will apply nanotechnology coatings on surfaces to prevent growth and spread of bacteria, viruses, mold etc. We deal with large corporates, airlines, hospitals and schools so we are after a new modern, simple and clean look that will have great visual impact.
We a company that is focused on prevention and protection.

Company name, Quorvane Systems Worldwide

Subtext, Antimicrobial Surface Protection

Logo, QVSW or QSW

Target Market(s)

Hospitals, Transport agencies, Airlines, Corporate entities

Industry/Entity Type

Protection

Contact Information for Business Card

Logo, QVSW or QSW
www.qvsw-example.us
Derek Holloway
+64290536218
tidyshieldnz@mailbox-example.com

Logo Text

QVSW

Requirements
Must have
• Simple clean look
Should not have
• Nothing too messy

```html
<!DOCTYPE html>
<html lang="en">
<head>
<meta charset="utf-8">
<title>Quorvane Systems Worldwide – Business Card</title>
<link rel="stylesheet" href="https://fonts.googleapis.com/css2?family=Oswald:wght@300;400;600&family=Open+Sans:wght@400;600&display=swap">
<style>
  :root {
    --canvas: #d9dadb;
    --card-dark: #26282b;
    --card-light: #eef0f2;
    --teal: #1fa3b2;
    --teal-soft: #cfe4e8;
    --ink: #1d1e20;
    --white: #ffffff;
    --muted: #9a9da1;
  }
  * { margin: 0; padding: 0; box-sizing: border-box; }
  html, body { width: 1200px; height: 857px; overflow: hidden; }
  body { background: var(--canvas); position: relative; font-family: "Open Sans", sans-serif; }

  .card {
    position: absolute; width: 520px; height: 300px;
    border-radius: 18px; overflow: hidden;
    box-shadow: 0 10px 24px rgba(0,0,0,.18);
  }
  .card svg.bands { position: absolute; inset: 0; width: 100%; height: 100%; }

  /* front */
  .card-front { left: 70px; top: 110px; background: var(--card-dark); }
  .front-lockup {
    position: absolute; left: 70px; top: 112px;
    display: flex; align-items: center; gap: 18px;
  }
  .logo-mark { display: flex; align-items: center; gap: 10px; }
  .logo-square { width: 22px; height: 22px; background: var(--teal); }
  .logo-word {
    font-family: "Oswald", sans-serif; font-weight: 600;
    font-size: 56px; line-height: 1; letter-spacing: 1px;
  }
  .card-front .logo-word { color: var(--white); }
  .company { color: var(--white); font-family: "Oswald", sans-serif; }
  .company-name { font-weight: 400; font-size: 21px; line-height: 1.15; }
  .company-sub {
    font-weight: 300; font-size: 10px; letter-spacing: 2px;
    color: #d6d8da; margin-top: 4px;
  }

  /* back */
  .card-back { left: 610px; top: 450px; background: var(--card-light); }
  .holder { position: absolute; right: 34px; top: 34px; text-align: left; }
  .holder-name {
    font-family: "Oswald", sans-serif; font-weight: 400;
    font-size: 19px; letter-spacing: 5px; color: var(--ink);
  }
  .holder-role { font-size: 10px; font-weight: 600; color: var(--ink); margin-top: 2px; padding-left: 92px; }
  .holder-rule { width: 86px; height: 5px; background: var(--ink); margin-top: -8px; }

  .contacts { position: absolute; right: 30px; top: 108px; display: flex; flex-direction: column; gap: 10px; align-items: flex-end; }
  .contact { display: flex; align-items: center; gap: 8px; font-size: 10px; font-weight: 600; color: var(--ink); }
  .icon { width: 22px; height: 22px; border-radius: 50%; background: var(--ink); display: flex; align-items: center; justify-content: center; }
  .icon svg { width: 13px; height: 13px; }

  .back-logo { position: absolute; left: 96px; top: 160px; }
  .card-back .logo-word { color: var(--ink); font-size: 60px; }
</style>
</head>
<body>

<section class="card card-front" aria-label="Card front">
  <svg class="bands" viewBox="0 0 520 300" preserveAspectRatio="none" aria-hidden="true">
    <defs>
      <linearGradient id="frontTop" x1="1" y1="0" x2="0" y2="0">
        <stop offset="0" stop-color="#1fa3b2"/>
        <stop offset=".55" stop-color="#2f4c52"/>
        <stop offset="1" stop-color="#26282b"/>
      </linearGradient>
      <linearGradient id="frontBottom" x1="0" y1="0" x2="1" y2="0">
        <stop offset="0" stop-color="#c3c6c8"/>
        <stop offset=".6" stop-color="#55585b"/>
        <stop offset="1" stop-color="#26282b"/>
      </linearGradient>
    </defs>
    <path d="M0,0 H520 V30 H275 L255,44 H0 Z" fill="url(#frontTop)"/>
    <path d="M0,300 V262 H285 L305,244 H520 V300 Z" fill="url(#frontBottom)"/>
  </svg>
  <div class="front-lockup">
    <div class="logo-mark">
      <span class="logo-square"></span>
      <span class="logo-word">QVSW</span>
    </div>
    <div class="company">
      <div class="company-name">Quorvane Systems<br>Worldwide</div>
      <div class="company-sub">(Antimicrobial Surface Protection)</div>
    </div>
  </div>
</section>

<section class="card card-back" aria-label="Card back">
  <svg class="bands" viewBox="0 0 520 300" preserveAspectRatio="none" aria-hidden="true">
    <defs>
      <linearGradient id="backTop" x1="0" y1="0" x2="1" y2="0">
        <stop offset="0" stop-color="#e2e3e4"/>
        <stop offset=".7" stop-color="#5a5c5f"/>
        <stop offset="1" stop-color="#111213"/>
      </linearGradient>
      <linearGradient id="backBottom" x1="0" y1="1" x2="1" y2="0">
        <stop offset="0" stop-color="#1fa3b2"/>
        <stop offset=".6" stop-color="#9fcfd6"/>
        <stop offset="1" stop-color="#e6eff1"/>
      </linearGradient>
    </defs>
    <path d="M0,0 H520 V18 H292 L280,40 H0 Z" fill="url(#backTop)"/>
    <path d="M0,300 V268 H262 L272,240 H520 V300 Z" fill="url(#backBottom)"/>
  </svg>

  <div class="holder">
    <div class="holder-name">DEREK HOLLOWAY</div>
    <div class="holder-role">Managing Director</div>
    <div class="holder-rule"></div>
  </div>

  <div class="contacts">
    <div class="contact">tidyshieldnz@mailbox-example.com
      <span class="icon"><svg viewBox="0 0 16 16"><rect x="1.5" y="3.5" width="13" height="9" fill="none" stroke="#fff" stroke-width="1.4"/><path d="M1.5,3.5 L8,9 L14.5,3.5" fill="none" stroke="#fff" stroke-width="1.4"/></svg></span>
    </div>
    <div class="contact">
      <span class="icon"><svg viewBox="0 0 16 16"><circle cx="8" cy="8" r="6.5" fill="none" stroke="#fff" stroke-width="1.2"/><ellipse cx="8" cy="8" rx="3" ry="6.5" fill="none" stroke="#fff" stroke-width="1.2"/><path d="M1.5,8 H14.5 M2.5,4.8 H13.5 M2.5,11.2 H13.5" stroke="#fff" stroke-width="1.1"/></svg></span>
      www.qvsw-example.us
    </div>
    <div class="contact">+64290536218
      <span class="icon"><svg viewBox="0 0 16 16"><rect x="4.5" y="1.5" width="7" height="13" rx="1.3" fill="none" stroke="#fff" stroke-width="1.4"/><circle cx="8" cy="12" r=".9" fill="#fff"/></svg></span>
    </div>
  </div>

  <div class="back-logo logo-mark">
    <span class="logo-square"></span>
    <span class="logo-word">QVSW</span>
  </div>
</section>

</body>
</html>
```